Personal Training Studio business cards

Black logo on front. Also need: Carlyse Brondway Master Trainer, Phone: 0498315627 on the front.
On the back want the white logo and also want 10 stars or similar that can be stamped when attended Studio. The 10th start to have "Free" written under it.
Also want a line to write an appointment date and time on it.

```html
<!DOCTYPE html>
<html lang="en">
<head>
<meta charset="utf-8">
<title>Pulse Six – Business Cards</title>
<link rel="stylesheet" href="https://fonts.googleapis.com/css2?family=Montserrat:wght@400;600;800&family=Quicksand:wght@400;500;700&display=swap">
<style>
  :root {
    --stage: #d4d4d4;
    --purple: #66309a;
    --purple-soft: #6b4aa3;
    --green: #7dc242;
    --green-bright: #8cc63f;
    --ink-dark: #161616;
    --white: #ffffff;
    --star: #f2b619;
    --star-edge: #c98a0a;
  }
  * { box-sizing: border-box; margin: 0; padding: 0; }
  html, body {
    width: 1200px; height: 1000px; overflow: hidden;
    background: var(--stage);
  }
  .canvas { position: relative; width: 1200px; height: 1000px; }

  .card {
    position: absolute; left: 241px; width: 683px; height: 410px;
    overflow: hidden;
  }
  .card--front { top: 74px; }
  .card--back  { top: 529px; }

  .card__photo { position: absolute; inset: 0; }
  .card--front .card__photo {
    background: linear-gradient(120deg, #1c1c1c 0%, #262626 45%, #3a302b 72%, #1d1d1d 100%);
  }
  .card--back .card__photo {
    background: linear-gradient(120deg, #e9e8ef 0%, #dcdbe6 45%, #d9cfc9 70%, #e4e3ea 100%);
  }

  .rule { position: absolute; background: var(--green); }

  .brand {
    position: absolute; left: 0; right: 0;
    display: flex; align-items: center; justify-content: center; gap: 12px;
    font-family: "Montserrat", sans-serif; font-weight: 800;
    letter-spacing: 1px;
  }
  .brand__dot { width: 26px; height: 26px; border-radius: 50%; }

  .card--front .brand { top: 95px; font-size: 44px; color: var(--purple-soft); }
  .card--front .brand__dot { background: var(--purple-soft); }

  .name-plate {
    position: absolute; left: 47px; top: 241px; width: 590px; height: 78px;
    background: var(--purple); color: var(--white); text-align: center;
    font-family: "Quicksand", sans-serif;
  }
  .name-plate__name { margin-top: 8px; font-size: 27px; font-weight: 500; }
  .name-plate__name strong { font-weight: 700; }
  .name-plate__role { margin-top: 7px; font-size: 17px; font-weight: 500; }

  .phone {
    position: absolute; left: 0; right: 0; top: 366px; text-align: center;
    font-family: "Quicksand", sans-serif; font-size: 15px; color: #d8d8d8;
    letter-spacing: 0.5px;
  }

  .ribbon { position: absolute; top: 132px; width: 160px; height: 95px; }
  .ribbon--left { left: 0; }
  .ribbon--right { right: 0; }

  .card--back .brand { top: 110px; font-size: 48px; color: var(--purple); }
  .card--back .brand__dot { background: var(--purple); }

  .stamps { position: absolute; left: 200px; top: 258px; }
  .stamps__free {
    position: absolute; left: 464px; top: 290px;
    font-family: "Montserrat", sans-serif; font-weight: 800; font-size: 12px;
    color: var(--purple);
  }

  .appointment__line { position: absolute; left: 11px; width: 661px; height: 4px; background: var(--purple); }
  .appointment__band {
    position: absolute; left: 0; top: 365px; width: 683px; height: 22px;
    background: var(--green-bright); color: var(--white);
    font-family: "Montserrat", sans-serif; font-weight: 800; font-size: 14px;
    display: flex; align-items: center; gap: 33px; padding-left: 102px;
  }
</style>
</head>
<body>
<div class="canvas">

  <section class="card card--front">
    <div class="card__photo" role="img" aria-label="Dim gym interior with a trainer lifting a dumbbell on a bench"></div>
    <div class="rule" style="left:23px; top:32px; width:636px; height:3px;"></div>
    <div class="rule" style="left:19px; top:46px; width:3px; height:318px;"></div>
    <div class="rule" style="left:661px; top:46px; width:3px; height:318px;"></div>
    <div class="rule" style="left:23px; top:374px; width:260px; height:3px;"></div>
    <div class="rule" style="left:397px; top:374px; width:262px; height:3px;"></div>

    <div class="brand"><span class="brand__dot"></span>PULSE SIX</div>

    <div class="rule" style="left:59px; top:231px; width:565px; height:9px;"></div>
    <div class="name-plate">
      <p class="name-plate__name"><strong>Carlyse</strong> Brondway</p>
      <p class="name-plate__role">Master Trainer</p>
    </div>
    <div class="rule" style="left:59px; top:321px; width:565px; height:9px;"></div>

    <p class="phone">0498315627</p>
  </section>

  <section class="card card--back">
    <div class="card__photo" role="img" aria-label="Bright gym interior with a trainer lifting a dumbbell on a bench"></div>

    <svg class="ribbon ribbon--left" viewBox="0 0 160 95" aria-hidden="true">
      <polygon points="0,0 95,0 155,95 0,95" fill="var(--purple-soft)"/>
      <polygon points="95,0 125,0 112,27" fill="var(--green)"/>
    </svg>
    <svg class="ribbon ribbon--right" viewBox="0 0 160 95" aria-hidden="true">
      <polygon points="60,0 160,0 160,95 5,95" fill="var(--purple-soft)"/>
      <polygon points="5,95 50,95 38,55" fill="var(--green)"/>
    </svg>

    <div class="brand"><span class="brand__dot"></span>PULSE SIX</div>

    <svg class="stamps" width="302" height="30" viewBox="0 0 302 30" role="img" aria-label="Ten visit stamps">
      <defs>
        <symbol id="star" viewBox="0 0 30 30">
          <polygon points="15,1 19,11 29,11.5 21,18 24,28.5 15,22.5 6,28.5 9,18 1,11.5 11,11"
                   fill="var(--star)" stroke="var(--star-edge)" stroke-width="1"/>
        </symbol>
      </defs>
      <use href="#star" x="0" width="30" height="30"/>
      <use href="#star" x="30" width="30" height="30"/>
      <use href="#star" x="60" width="30" height="30"/>
      <use href="#star" x="90" width="30" height="30"/>
      <use href="#star" x="120" width="30" height="30"/>
      <use href="#star" x="150" width="30" height="30"/>
      <use href="#star" x="180" width="30" height="30"/>
      <use href="#star" x="210" width="30" height="30"/>
      <use href="#star" x="240" width="30" height="30"/>
      <use href="#star" x="270" width="30" height="30"/>
    </svg>
    <p class="stamps__free">FREE</p>

    <div class="appointment__line" style="top:357px;"></div>
    <div class="appointment__band">
      <span>APPOINTMENT:</span><span>DATE (00/00/00)</span><span>TIME (00:00)</span>
    </div>
    <div class="appointment__line" style="top:390px;"></div>
  </section>

</div>
</body>
</html>
```